Keystone Networks, it support and management

We run an IT business, so techy style would work well. We need a re-design, now that we’ve moved and phone numbers have changed.

On the back of the card I like having something that helps with taking notes, like a grid or lines

The attachment is the current business card I am using.

We specialize in helping out in all kinds of support, including laptops, desktops, servers, and providing software solutions, like deskpro 480, backups and ransomware prevention

Target Market(s)

Other small business owners, specifically smaller than 50 employees

Industry/Entity Type

SMB, but no specific niche

Contact Information for Business Card

I’d like the logo, name, my title/rolw, my contact details

Colors
0094D4
00A9DD
6FCCEA
C7EBF8
E9F6FB

Requirements
Must have
• The ability to take notes on the back of the card
Nice to have
• A new slogan or fun little quip, but not necessary
Should not have
• Street address of any kind.

```html
<!DOCTYPE html>
<html lang="en">
<head>
<meta charset="utf-8">
<title>Keystone Networks – Business Card</title>
<link rel="stylesheet" href="https://fonts.googleapis.com/css2?family=Arimo:wght@400;700&display=swap">
<style>
  :root {
    --backdrop: #e0e0de;
    --card-white: #ffffff;
    --card-dark: #2f2f30;
    --brand-blue: #5a6b9e;
    --ink-dark: #2b2b2b;
    --ink-grey: #7b7b7b;
    --rule-grey: #9a9a9a;
    --watermark: #ececec;
    --disc-dark: #222223;
    --note-line: #4a4a4c;
  }
  * { box-sizing: border-box; margin: 0; padding: 0; }
  html, body { width: 1200px; height: 802px; overflow: hidden; }
  body {
    background: var(--backdrop);
    font-family: "Arimo", Arial, sans-serif;
    position: relative;
  }
  .card {
    position: absolute;
    width: 520px;
    height: 297px;
    border-bottom: 3px solid var(--brand-blue);
    overflow: hidden;
  }
  /* Front */
  .card-front { left: 60px; top: 150px; background: var(--card-white); }
  .card-front .watermark-disc {
    position: absolute; left: 30px; top: 150px;
    width: 230px; height: 230px; border-radius: 50%;
    background: var(--watermark);
  }
  .brand {
    position: absolute; right: 34px; top: 40px;
    display: flex; align-items: center; gap: 12px;
  }
  .brand-dot {
    width: 26px; height: 26px; border-radius: 50%;
    background: var(--ink-dark);
  }
  .brand-name {
    color: var(--brand-blue); font-weight: 700; font-size: 30px; letter-spacing: 0.5px;
  }
  .brand-rule {
    position: absolute; right: 34px; top: 88px; width: 300px;
    border-top: 1px solid var(--rule-grey);
  }
  .person { position: absolute; left: 34px; top: 166px; }
  .person-name { color: var(--brand-blue); font-weight: 700; font-size: 19px; letter-spacing: 0.3px; }
  .person-title { color: var(--ink-grey); font-size: 13px; margin-top: 2px; }
  .person-rule { width: 260px; border-top: 1px solid var(--rule-grey); margin-top: 6px; }
  .contacts { position: absolute; left: 34px; top: 218px; list-style: none; }
  .contacts li {
    display: flex; align-items: center; gap: 8px;
    color: var(--ink-grey); font-size: 13px; line-height: 17px;
  }
  .contacts svg { width: 11px; height: 11px; flex: none; }
  /* Back */
  .card-back { left: 620px; top: 355px; background: var(--card-dark); }
  .card-back .back-disc {
    position: absolute; right: 36px; top: 36px;
    width: 200px; height: 200px; border-radius: 50%;
    background: var(--disc-dark);
  }
  .notes {
    position: absolute; left: 36px; top: 44px; width: 210px;
    list-style: none;
  }
  .notes li {
    height: 26px;
    border-bottom: 1px solid var(--note-line);
  }
  .card-back .brand-name-large {
    position: absolute; left: 36px; bottom: 40px;
    color: var(--brand-blue); font-weight: 700; font-size: 34px;
  }
</style>
</head>
<body>
  <section class="card card-front" aria-label="Business card front">
    <div class="watermark-disc"></div>
    <div class="brand">
      <span class="brand-dot"></span>
      <span class="brand-name">Keystone Networks</span>
    </div>
    <div class="brand-rule"></div>
    <div class="person">
      <p class="person-name">DANA WHITFIELD</p>
      <p class="person-title">President</p>
      <div class="person-rule"></div>
    </div>
    <ul class="contacts">
      <li><svg viewBox="0 0 12 12"><path d="M3 1l2 2-1 1.5c.6 1.4 1.8 2.6 3.2 3.2L8.7 6.7l2 2-1.2 1.8C5.3 10.5 1.5 6.7 1.2 2.5z" fill="var(--brand-blue)"/></svg>555.201.4830 x 118</li>
      <li><svg viewBox="0 0 12 12"><rect x="3" y="0.8" width="6" height="10.4" rx="1" fill="none" stroke="var(--brand-blue)" stroke-width="1.2"/></svg>555.384.2271</li>
      <li><svg viewBox="0 0 12 12"><rect x="0.8" y="2.5" width="10.4" height="7" fill="none" stroke="var(--brand-blue)" stroke-width="1.2"/><path d="M1 3l5 3.6L11 3" fill="none" stroke="var(--brand-blue)" stroke-width="1.2"/></svg>danaw@keystonenw.com</li>
      <li><svg viewBox="0 0 12 12"><circle cx="6" cy="6" r="5" fill="none" stroke="var(--brand-blue)" stroke-width="1.2"/><path d="M1 6h10M6 1c-2.5 3-2.5 7 0 10M6 1c2.5 3 2.5 7 0 10" fill="none" stroke="var(--brand-blue)" stroke-width="1"/></svg>www.keystonenw.com</li>
    </ul>
  </section>

  <section class="card card-back" aria-label="Business card back">
    <div class="back-disc"></div>
    <ul class="notes" aria-label="Lines for notes">
      <li></li><li></li><li></li><li></li><li></li>
    </ul>
    <span class="brand-name-large">Keystone Networks</span>
  </section>
</body>
</html>
```